Small Business Broker Business Card Design

A business card design for a small business brokerage, which is a financial service, not unlike real estate brokerage, but for small businesses such as laundromats, pizza shops, restaurants, cleaners etc. The designs should all be simple, more conservative in nature, using the colors and font of the logo. Again, think real estate Brokerage as a business context
Contact Information for Business Card
Name: Milo R. Dunbar. Title: Small Business Advisor. Email: m.dunbar@harborstoneadvisory.com. Mobile: (917) 555-0148. Office: (718) 555-0193. www.harborstoneadvisory.com

```html
<!DOCTYPE html>
<html lang="en">
<head>
<meta charset="utf-8">
<title>Harborstone Advisory – Business Card</title>
<link rel="stylesheet" href="https://fonts.googleapis.com/css2?family=League+Spartan:wght@400;500;600&display=swap">
<style>
  :root {
    --navy: #1f3b6c;
    --green: #8dc63f;
    --paper: #ffffff;
    --stage: #e9e9e9;
    --card-shadow: 0 4px 12px rgba(0,0,0,0.25);
  }
  * { box-sizing: border-box; margin: 0; padding: 0; }
  html, body { width: 1200px; height: 900px; overflow: hidden; }
  body {
    background: var(--stage);
    font-family: "League Spartan", "Helvetica Neue", Arial, sans-serif;
    position: relative;
  }
  .card {
    position: absolute;
    top: 300px;
    width: 532px;
    height: 306px;
    background: var(--paper);
    box-shadow: var(--card-shadow);
    overflow: hidden;
  }
  .card--front { left: 58px; }
  .card--back { left: 612px; }

  /* Front */
  .front-lockup {
    position: absolute;
    left: 0; right: 0; top: 88px;
    text-align: center;
  }
  .front-lockup__mark {
    display: block;
    width: 64px; height: 64px;
    margin: 0 auto 22px;
    background: var(--navy);
  }
  .front-lockup__name {
    color: var(--navy);
    font-weight: 600;
    font-size: 21px;
    letter-spacing: 0.04em;
    text-transform: uppercase;
  }
  .front-lockup__tagline {
    margin-top: 4px;
    color: var(--green);
    font-weight: 500;
    font-size: 10.5px;
    letter-spacing: 0.14em;
    text-transform: uppercase;
  }

  /* Back */
  .person { position: absolute; left: 33px; top: 46px; }
  .person__name {
    color: var(--navy);
    font-weight: 600;
    font-size: 24px;
    letter-spacing: 0.03em;
    text-transform: uppercase;
  }
  .person__title {
    margin-top: 2px;
    color: var(--green);
    font-weight: 500;
    font-size: 13px;
    letter-spacing: 0.06em;
    text-transform: uppercase;
  }
  .back-brand {
    position: absolute;
    right: 34px; top: 50px;
    color: var(--navy);
    font-weight: 600;
    font-size: 14px;
    letter-spacing: 0.06em;
    text-transform: uppercase;
    text-align: right;
  }
  .contact {
    position: absolute;
    left: 45px; top: 183px;
    list-style: none;
  }
  .contact__row { display: flex; align-items: baseline; height: 19.5px; }
  .contact__label {
    width: 59px;
    color: var(--green);
    font-weight: 500;
    font-size: 12.5px;
    letter-spacing: 0.08em;
    text-transform: uppercase;
  }
  .contact__value {
    color: var(--navy);
    font-weight: 500;
    font-size: 15px;
    letter-spacing: 0.03em;
  }
  .contact__value--email { text-transform: uppercase; }
  .footer-band {
    position: absolute;
    left: 0; right: 0; bottom: 0;
    height: 56px;
    background: var(--navy);
    border-top: 5px solid var(--green);
    display: flex;
    align-items: center;
    padding-left: 45px;
  }
  .footer-band__web {
    color: var(--green);
    font-weight: 500;
    font-size: 14px;
    letter-spacing: 0.06em;
    text-transform: uppercase;
    padding-top: 3px;
  }
</style>
</head>
<body>
  <section class="card card--front" aria-label="Card front">
    <div class="front-lockup">
      <span class="front-lockup__mark" aria-hidden="true"></span>
      <h1 class="front-lockup__name">Harborstone Advisory, Inc</h1>
      <p class="front-lockup__tagline">Trusted guidance for buying and selling business</p>
    </div>
  </section>

  <section class="card card--back" aria-label="Card back">
    <div class="person">
      <h2 class="person__name">Milo R. Dunbar</h2>
      <p class="person__title">Small Business Advisor</p>
    </div>
    <p class="back-brand">Harborstone<br>Advisory</p>
    <ul class="contact">
      <li class="contact__row"><span class="contact__label">Office:</span><span class="contact__value">(718) 555-0193</span></li>
      <li class="contact__row"><span class="contact__label">Mobile:</span><span class="contact__value">(917) 555-0148</span></li>
      <li class="contact__row"><span class="contact__label">Email:</span><span class="contact__value contact__value--email">m.dunbar@harborstoneadvisory.com</span></li>
    </ul>
    <div class="footer-band">
      <span class="footer-band__web">www.harborstoneadvisory.com</span>
    </div>
  </section>
</body>
</html>
```